MS Word Template needed for a company specialized in Insurance and Finance Advising

I am looking for an impressive and memorable Word Template for:

Writing daily letters
Presentations
Agreements
Front Pages for Projects
Finance, pension, tax analyzes ...

Our logo is attached.
We are advising clients in all kind of questions in the finance and insurance industry, we are not selling products, our main business is the advising and to win the trust to all kind of costumers, from young to old from all kind of nations.

```html
<!DOCTYPE html>
<html lang="en">
<head>
<meta charset="utf-8">
<title>Meridian Advisory – Document Template</title>
<link href="https://fonts.googleapis.com/css2?family=Montserrat:wght@400;500;700&family=Roboto:wght@400;500;700&display=swap" rel="stylesheet">
<style>
:root{
  --red:#f50a0a;
  --red-soft:rgba(240,30,30,.78);
  --ink:#222;
  --grey:#6e6e6e;
  --grey-mid:#8a8a8a;
  --grey-light:#efeded;
  --band:#f2f2f2;
  --page:#fff;
  --canvas:#ffffff;
}
*{box-sizing:border-box;margin:0;padding:0}
html,body{width:1200px;height:1056px;overflow:hidden;background:var(--canvas);font-family:"Roboto",Arial,sans-serif;color:var(--ink)}
.spread{position:relative;width:1200px;height:1056px}
.page{position:absolute;width:368px;height:474px;background:var(--page);box-shadow:0 6px 18px rgba(0,0,0,.18);overflow:hidden}
.p1{left:32px;top:41px}.p2{left:416px;top:38px}.p3{left:798px;top:37px}
.p4{left:34px;top:529px}.p5{left:415px;top:529px}.p6{left:797px;top:528px}

/* header & footer */
.page-header{position:absolute;left:0;top:0;width:100%;height:40px}
.brand{position:absolute;right:8px;top:13px;font:700 13px "Roboto",sans-serif;color:var(--red);letter-spacing:.3px}
.brand-dot{display:inline-block;width:6px;height:6px;border-radius:50%;background:var(--red);margin-right:3px;vertical-align:middle}
.page-footer{position:absolute;left:10px;right:12px;bottom:16px;height:13px;background:var(--grey-mid);color:#fff;font-size:4.6px;line-height:13px;padding-left:3px}
.page-footer .num{position:absolute;right:0;top:0;width:36px;height:13px;background:var(--red);text-align:center;font-size:7px}

.section-mark{position:absolute;left:0;width:20px;height:26px;background:var(--red)}
.section-title{position:absolute;font:500 15px "Roboto",sans-serif;color:#555}
.body{font-size:6.6px;line-height:8.2px;text-align:justify;color:#222}

/* cover */
.cover-photo{position:absolute;inset:0;background:linear-gradient(135deg,#3a3f4c 0%,#6b5a55 35%,#2c2f38 60%,#8b6b55 100%)}
.cover-panel{position:absolute;left:26px;top:218px;width:237px;height:256px;background:var(--red-soft)}
.cover-brand{position:absolute;left:0;right:0;top:24px;text-align:center;font:700 16px "Montserrat",sans-serif;color:var(--red)}
.cover-title{position:absolute;left:17px;top:28px;font:700 36px/37px "Montserrat",sans-serif;color:#fff}
.cover-rule{position:absolute;left:17px;top:111px;width:185px;height:3px;background:#bdbdbd}
.cover-kicker{position:absolute;left:18px;top:130px;font:500 10px "Montserrat",sans-serif;color:#fff;letter-spacing:.5px}
.cover-name{position:absolute;left:18px;top:156px;font:500 13px "Montserrat",sans-serif;color:#fff}
.cover-contact{position:absolute;left:17px;top:177px;font:400 6px/9.5px "Montserrat",sans-serif;color:#fff}

/* contents */
.toc-bg{position:absolute;left:0;top:62px;width:368px;height:358px;background:var(--grey-light)}
.toc-photo{position:absolute;left:218px;top:62px;width:150px;height:358px;background:linear-gradient(160deg,#9fc6e6,#4d7ba6 55%,#1e3550)}
.toc-head{position:absolute;left:63px;top:101px;width:186px;height:35px;background:var(--red);color:#fff;font:700 16px/35px "Roboto",sans-serif;padding-left:13px}
.toc-chapter{position:absolute;left:68px;top:153px;font:400 11.5px "Montserrat",sans-serif;color:var(--red)}
.toc-list{position:absolute;left:66px;top:180px;list-style:none;font:400 6.6px "Montserrat",sans-serif;color:#333}
.toc-list li{height:18px}
.toc-list span{display:inline-block;width:18px}

/* industry page */
.p3-text{position:absolute;left:35px;width:148px}
.chart{position:absolute;left:34px;top:199px;width:150px;height:150px;border:1px solid #ccc}
.side-panel{position:absolute;left:200px;top:50px;width:147px;height:364px;background:var(--grey-light);padding:14px 13px}
.side-panel h3{font:500 11px "Roboto",sans-serif;color:var(--red);margin-bottom:1px}
.side-panel p{font-size:6.5px;line-height:8.2px;text-align:justify;margin-bottom:12px}

/* table page */
.data-table{position:absolute;left:30px;top:91px;width:317px;border-collapse:collapse;font-size:6.8px}
.data-table th{background:var(--red);color:#fff;text-align:left;font-weight:700;height:13px;padding-left:3px;border:1px solid #888}
.data-table td{height:15.6px;padding-left:3px;border:1px solid #999}
.data-table td:first-child{font-weight:700}
.sub-title{position:absolute;left:30px;font:500 14px "Roboto",sans-serif;color:#555}
.p4-text{position:absolute;left:30px;width:310px}

/* lorem page */
.ring-row{position:absolute;left:20px;top:162px;width:320px;height:92px}
.ring-text{position:absolute;top:30px;width:60px;text-align:center;font:400 7px/10px "Montserrat",sans-serif;color:#777}
.project{position:absolute;width:140px}
.project h4{font:700 8.6px "Roboto",sans-serif;color:var(--red);margin:0 0 5px 22px}
.project p{font:400 7px/10.2px "Montserrat",sans-serif;color:#888;margin-left:22px}
.tick{position:absolute;left:0;top:-3px}

/* gallery page */
.photo{position:absolute;left:0;width:302px;height:178px}
.photo-a{top:57px;background:linear-gradient(120deg,#3f4754,#7d6a62 50%,#2e3440)}
.photo-b{top:236px;background:linear-gradient(120deg,#d9c8b8,#a47c62 45%,#eee5dc)}
.photo-card{position:absolute;left:175px;width:127px;background:#fff}
.photo-card h5{height:23px;background:var(--red);color:#fff;font:700 8.6px/23px "Roboto",sans-serif;padding-left:16px}
.photo-card p{font:400 6.2px/9.8px "Montserrat",sans-serif;color:#222;padding:8px 12px 0 12px;background:#fff;height:82px}
</style>
</head>
<body>
<main class="spread">

<!-- cover -->
<section class="page p1">
  <div class="cover-photo" role="img" aria-label="Photo of advisors in a meeting with laptops, hands gesturing across a table"></div>
  <div class="cover-brand"><span class="brand-dot"></span>MERIDIAN ADVISORY</div>
  <div class="cover-panel">
    <h1 class="cover-title">Add title<br>here</h1>
    <div class="cover-rule"></div>
    <p class="cover-kicker">ADVISING</p>
    <p class="cover-name">Meridian Advisory</p>
    <p class="cover-contact">208 Harbor Road, Dover, DE 1990<br>302-555-0147<br>hello@meridianadvisory.com</p>
  </div>
</section>

<!-- contents -->
<section class="page p2">
  <svg class="page-header" viewBox="0 0 368 40" aria-hidden="true"><rect width="368" height="38" fill="#f2f2f2"/><path d="M0 12H185C200 12 210 20 196 30H0Z" fill="#f50a0a"/></svg>
  <div class="brand"><span class="brand-dot"></span>MERIDIAN ADVISORY</div>
  <div class="toc-bg"></div>
  <div class="toc-photo" role="img" aria-label="Photo of a hand pointing at a glass wall covered with sticky notes"></div>
  <h2 class="toc-head">Content Table</h2>
  <p class="toc-chapter">CHAPTER</p>
  <ol class="toc-list">
    <li><span>3</span>INTRODUCTION</li><li><span>4</span>ABOUT US</li><li><span>5</span>OUR TEAM</li>
    <li><span>6</span>OUR SERVICES</li><li><span>7</span>PORTFOLIO</li><li><span>8</span>PROPOSAL</li>
    <li><span>9</span>PROJECT TIMELINE</li><li><span>10</span>PROJECT COST</li><li><span>11</span>ANALYSIS</li>
    <li><span>12</span>PROCUREMENT</li>
  </ol>
  <footer class="page-footer">YOUR COMPANY NAME (C) COPYRIGHT (PRINT DATE) ALL RIGHTS RESERVED<span class="num">2</span></footer>
</section>

<!-- industry structure -->
<section class="page p3">
  <svg class="page-header" viewBox="0 0 368 40" aria-hidden="true"><rect width="368" height="38" fill="#f2f2f2"/><path d="M0 12H185C200 12 210 20 196 30H0Z" fill="#f50a0a"/></svg>
  <div class="brand"><span class="brand-dot"></span>MERIDIAN ADVISORY</div>
  <div class="section-mark" style="top:46px;width:24px"></div>
  <h2 class="section-title" style="left:30px;top:49px">1. Industry structure</h2>
  <p class="p3-text body" style="top:81px">Lorem ipsum dolor sit amet, consectetuer adipiscing elit, sed diam nonummy nibh euismod tincidunt ut laoreet dolore magna aliquam erat volutpat. Ut wisi enim ad minim veniam, quis nostrud exerci tation ullamcorper suscipit lobortis nisl ut aliquip ex ea commodo.</p>
  <p class="p3-text body" style="top:137px">Duis autem vel eum iriure dolor in hendrerit in vulputate velit esse molestie consequat, vel illum dolore eu feugiat nulla facilisis at vero eros et accumsan et iusto odio dignissim qui blandit present luptatum zzril delenit augue.</p>
  <svg class="chart" viewBox="0 0 150 150" aria-label="Bar chart across four categories">
    <g font-size="5" fill="#333" font-family="Roboto,sans-serif">
      <text x="4" y="8">6</text><text x="4" y="30">5</text><text x="4" y="51">4</text><text x="4" y="72">3</text><text x="4" y="94">2</text><text x="4" y="115">1</text><text x="4" y="137">0</text>
      <text x="14" y="145">Category 1</text><text x="47" y="145">Category 2</text><text x="80" y="145">Category 3</text><text x="113" y="145">Category 4</text>
    </g>
    <line x1="11" y1="135" x2="143" y2="135" stroke="#888" stroke-width=".6"/>
    <line x1="11" y1="6" x2="11" y2="135" stroke="#888" stroke-width=".6"/>
    <g>
      <rect x="18" y="42" width="7" height="93" fill="#f50a0a"/><rect x="26" y="83" width="6" height="52" fill="#cfcfcf"/><rect x="33" y="92" width="6" height="43" fill="#444"/>
      <rect x="51" y="81" width="7" height="54" fill="#f50a0a"/><rect x="59" y="41" width="6" height="94" fill="#cfcfcf"/><rect x="66" y="92" width="6" height="43" fill="#444"/>
      <rect x="84" y="60" width="7" height="75" fill="#f50a0a"/><rect x="92" y="96" width="6" height="39" fill="#cfcfcf"/><rect x="99" y="71" width="6" height="64" fill="#444"/>
      <rect x="117" y="38" width="7" height="97" fill="#f50a0a"/><rect x="125" y="74" width="6" height="61" fill="#cfcfcf"/><rect x="132" y="28" width="6" height="107" fill="#444"/>
    </g>
  </svg>
  <p class="p3-text body" style="top:362px;left:38px;width:145px;line-height:10px">Lorem ipsum dolor sit amet, consectetuer adipiscing elit, sed diam nonummy nibh euismod tincidunt ut laoreet dolore magna aliquam erat volutpat. Ut wisi enim ad minim veniam, quis nostrud exerci tation ullam</p>
  <aside class="side-panel">
    <h3>INNOVATE</h3>
    <p>Lorem Ipsum is simply dummy text of the printing and typesetting industry. Lorem Ipsum has been the industry's standard dummy text ever since the 1500s, when an unknown printer took a galley of type and scrambled it to make a type specimen book. It has survived not only five centuries, but also the leap into electronic typesetting, remaining essentially unchanged. It was popularised in the 1960s with the release of Transferset sheets containing Lorem Ipsum passages, and more recently with desktop publishing software like Folio Layout including versions of Lorem Ipsum.</p>
    <h3>STAY FOCUSED</h3>
    <p>Lorem Ipsum is simply dummy text of the printing and typesetting industry. Lorem Ipsum has been the industry's standard dummy text ever since the 1500s, when an unknown printer took a galley of type and scrambled it to make a type specimen book. It has survived not only five centuries, but also the leap into electronic typesetting, remaining essentially unchanged. It was popularised in the 1960s with the release of Transferset sheets containing Lorem Ipsum passages, and more recently with desktop publishing software like Folio Layout including versions of Lorem Ipsum.</p>
  </aside>
  <footer class="page-footer">YOUR COMPANY NAME (C) COPYRIGHT (PRINT DATE) ALL RIGHTS RESERVED<span class="num">3</span></footer>
</section>

<!-- table example -->
<section class="page p4">
  <svg class="page-header" viewBox="0 0 368 40" aria-hidden="true"><rect width="368" height="38" fill="#f2f2f2"/><path d="M0 12H185C200 12 210 20 196 30H0Z" fill="#f50a0a"/></svg>
  <div class="brand"><span class="brand-dot"></span>MERIDIAN ADVISORY</div>
  <div class="section-mark" style="top:61px"></div>
  <h2 class="section-title" style="left:30px;top:67px">2. Table Example</h2>
  <table class="data-table">
    <thead><tr><th>Products</th><th>Count</th><th>Region</th><th>Price</th></tr></thead>
    <tbody>
      <tr><td>Product 1</td><td>524</td><td>USA</td><td>$2542.00</td></tr>
      <tr><td>Product 2</td><td>5214</td><td>Europe</td><td>$3567.00</td></tr>
      <tr><td>Product 3</td><td>23</td><td>Post-Soviet</td><td>$2781.00</td></tr>
      <tr><td>Product 4</td><td>237</td><td>China</td><td>$1456.00</td></tr>
      <tr><td>Product 5</td><td>83</td><td>Africa</td><td>$1657.00</td></tr>
      <tr><td>Product 6</td><td>2138</td><td>Latin America</td><td>$1156.00</td></tr>
    </tbody>
  </table>
  <p class="p4-text body" style="top:212px">Transferset sheets containing Lorem Ipsum make a type specimen book. It has survived not only five centuries, but also the leap into electronic typesetting, remaining essentially unchanged. It was popularised in the 1960s with the release of Transferset sheets containing Lorem Ipsum make a type specimen book, but also the leap into electronic typesetting, remaining essentially unchanged. It was popularised in the 1960s with the release of Transferset sheets containing Lorem Ipsum make a type specimen book. It has survived not only five centuries, but also the leap into electronic typesetting, remaining essentially</p>
  <h3 class="sub-title" style="top:282px">2.2. Distribution Strategy</h3>
  <p class="p4-text body" style="top:301px;line-height:9.6px">&nbsp;&nbsp;&nbsp;&nbsp;Lorem Ipsum is simply dummy text of the printing and typesetting industry. Lorem Ipsum has been the industry's standard dummy text ever since the 1500s, when an unknown printer took a galley of type and popularised of containing Lorem Ipsum passages, and more recently with desktop publishing software like Folio Layout including versions scrambled it to</p>
  <h3 class="sub-title" style="top:349px">2.3. Advertising and Promotion</h3>
  <p class="p4-text body" style="top:368px">&nbsp;&nbsp;&nbsp;&nbsp;Lorem Ipsum is simply dummy text of the printing and typesetting industry. Lorem Ipsum has been the industry's standard dummy text ever since the 1500s, when an unknown printer took a galley of type and scrambled it to make a type specimen book. It has survived not only five centuries, but also the leap, remaining essentially unchanged. It was popularised in the 1960s with the release of Transferset sheets containing Lorem Ipsum passages, and more recently with desktop publishing software like Folio Layout including versions scrambled it to</p>
  <footer class="page-footer">YOUR COMPANY NAME (C) COPYRIGHT (PRINT DATE) ALL RIGHTS RESERVED<span class="num">4</span></footer>
</section>

<!-- lorem ipsum -->
<section class="page p5">
  <svg class="page-header" viewBox="0 0 368 40" aria-hidden="true"><rect width="368" height="38" fill="#f2f2f2"/><path d="M0 12H185C200 12 210 20 196 30H0Z" fill="#f50a0a"/></svg>
  <div class="brand"><span class="brand-dot"></span>MERIDIAN ADVISORY</div>
  <div class="section-mark" style="top:61px;width:23px"></div>
  <h2 class="section-title" style="left:32px;top:67px">3. Lorem Ipsum</h2>
  <p class="body" style="position:absolute;left:30px;top:98px;width:310px;line-height:9.5px">&nbsp;&nbsp;&nbsp;&nbsp;&nbsp;&nbsp;&nbsp;Lorem Ipsum is simply dummy text of the printing and typesetting industry. Lorem Ipsum has been the industry's standard dummy text ever since the 1500s, when an unknown printer took a galley of type and popularised of containing Lorem Ipsum passages, and more recently with desktop publishing software like Folio</p>
  <div class="ring-row">
    <svg width="320" height="92" viewBox="0 0 320 92" aria-hidden="true">
      <circle cx="45" cy="46" r="39" fill="none" stroke="#f50a0a" stroke-width="8"/>
      <circle cx="122" cy="46" r="39" fill="none" stroke="#8a8a8a" stroke-width="8"/>
      <circle cx="199" cy="46" r="39" fill="none" stroke="#f50a0a" stroke-width="8"/>
      <circle cx="277" cy="46" r="39" fill="none" stroke="#8a8a8a" stroke-width="8"/>
    </svg>
    <p class="ring-text" style="left:15px">Lorem Ipsum is simply dummy unknown printer took.</p>
    <p class="ring-text" style="left:92px">Lorem Ipsum is simply dummy unknown printer took.</p>
    <p class="ring-text" style="left:169px">Lorem Ipsum is simply dummy unknown printer took.</p>
    <p class="ring-text" style="left:247px">Lorem Ipsum is simply dummy unknown printer took.</p>
  </div>
  <div class="project" style="left:28px;top:280px">
    <svg class="tick" width="17" height="17" viewBox="0 0 17 17" aria-hidden="true"><circle cx="8.5" cy="8.5" r="7" fill="none" stroke="#f50a0a" stroke-width="1.5"/><path d="M5 8.5l3 3 7-8" fill="none" stroke="#f50a0a" stroke-width="1.8"/></svg>
    <h4>Project name</h4><p>Lorem ipsum dolor sit amet, nec an dictas equidem appellantur, ut has commune accommodare. Mea illum, ludus solet idpro.</p>
  </div>
  <div class="project" style="left:180px;top:280px">
    <svg class="tick" width="17" height="17" viewBox="0 0 17 17" aria-hidden="true"><circle cx="8.5" cy="8.5" r="7" fill="none" stroke="#f50a0a" stroke-width="1.5"/><path d="M5 8.5l3 3 7-8" fill="none" stroke="#f50a0a" stroke-width="1.8"/></svg>
    <h4>Project name</h4><p>Lorem ipsum dolor sit amet, nec an dictas equidem appellantur, ut has commune accommodare. Mea illum, ludus solet idpro.</p>
  </div>
  <div class="project" style="left:28px;top:362px">
    <svg class="tick" width="17" height="17" viewBox="0 0 17 17" aria-hidden="true"><circle cx="8.5" cy="8.5" r="7" fill="none" stroke="#f50a0a" stroke-width="1.5"/><path d="M5 8.5l3 3 7-8" fill="none" stroke="#f50a0a" stroke-width="1.8"/></svg>
    <h4>Project name</h4><p>Lorem ipsum dolor sit amet, nec an dictas equidem appellantur, ut has commune accommodare. Mea illum, ludus solet idpro.</p>
  </div>
  <div class="project" style="left:180px;top:362px">
    <svg class="tick" width="17" height="17" viewBox="0 0 17 17" aria-hidden="true"><circle cx="8.5" cy="8.5" r="7" fill="none" stroke="#f50a0a" stroke-width="1.5"/><path d="M5 8.5l3 3 7-8" fill="none" stroke="#f50a0a" stroke-width="1.8"/></svg>
    <h4>Project name</h4><p>Lorem ipsum dolor sit amet, nec an dictas equidem appellantur, ut has commune accommodare. Mea illum, ludus solet idpro.</p>
  </div>
  <footer class="page-footer">YOUR COMPANY NAME (C) COPYRIGHT (PRINT DATE) ALL RIGHTS RESERVED<span class="num">5</span></footer>
</section>

<!-- gallery -->
<section class="page p6">
  <svg class="page-header" viewBox="0 0 368 40" aria-hidden="true"><rect width="368" height="38" fill="#f2f2f2"/><path d="M0 12H185C200 12 210 20 196 30H0Z" fill="#f50a0a"/></svg>
  <div class="brand"><span class="brand-dot"></span>MERIDIAN ADVISORY</div>
  <div class="photo photo-a" role="img" aria-label="Photo of a business meeting with people gesturing at a table"></div>
  <div class="photo photo-b" role="img" aria-label="Photo of two colleagues working at a laptop by a bright window"></div>
  <div class="photo-card" style="top:131px"><h5>LOREM IPSUM</h5><p>Lorem Ipsum is simply dummy text of the printing and typesetting industry. Lorem Ipsum has been the industry's standard dummy text ever since</p></div>
  <div class="photo-card" style="top:314px"><h5>LOREM IPSUM</h5><p>Lorem Ipsum is simply dummy text of the printing and typesetting industry. Lorem Ipsum has been the industry's standard dummy text ever since</p></div>
  <footer class="page-footer">YOUR COMPANY NAME (C) COPYRIGHT (PRINT DATE) ALL RIGHTS RESERVED<span class="num">6</span></footer>
</section>

</main>
</body>
</html>
```